Terraquest NW PPT template - non-profit company - minerals, energy, water, geothermal resources

Terraquest NW requires two (Letter-sized and 16:9)simple, flexible and clean PowerPoint templates that can be used for corporate and research project presentations and meeting materials

Each layout should have correct colours, fonts and size as a default (focus area colours for headings; secondary colours for body text). Each slide should have the Terraquest NW logo. Slide number should be automatically generated, with no slide number on title slide.

Target Market(s)

Varied, but almost always professional: Government; Community leaders; Mineral/Energy industries; and Academic researchers.

Font styles to use
Serif
Sans Serif
Other font styles liked:
• Calibri, or whatever in style guide

Requirements
Must have
• Two version that we can use – both need to match:
- 16:9 slide size for on-screen presentations; and
- Letter (8.5 x 11 inch) for meeting materials that are printed.

Must use colours in logo as listed in the style guide
Nice to have
• Consistency
Should not have
• Should not be black and white - needs colour

```html
<!DOCTYPE html>
<html lang="en">
<head>
<meta charset="utf-8">
<title>Terraquest NW – Presentation Template</title>
<link href="https://fonts.googleapis.com/css2?family=Hind:wght@400;500;600;700&family=Open+Sans:wght@400;600;700&display=swap" rel="stylesheet">
<style>
:root{
  --page:#e8e8e8;
  --slate:#56606b;
  --slate-dark:#454e58;
  --orange:#dd6a27;
  --orange-soft:#e98a4c;
  --green:#1fa84a;
  --lime:#7dc243;
  --blue:#27a6cc;
  --text:#8c8c8c;
  --ink:#4e555c;
  --white:#ffffff;
}
*{box-sizing:border-box;margin:0;padding:0}
html,body{width:1200px;height:2847px;overflow:hidden;background:var(--page)}
body{position:relative;font-family:"Open Sans",Arial,sans-serif;color:var(--ink)}
.slide{position:absolute;width:568px;height:320px;overflow:hidden;background:var(--white);box-shadow:0 6px 10px rgba(0,0,0,.18)}
.col-l{left:20px}.col-r{left:610px}
.r1{top:25px}.r2{top:378px}.r3{top:729px}.r4{top:1081px}.r5{top:1433px}.r6{top:1785px}.r7{top:2136px}.r8{top:2489px}
.brand{font-family:"Hind",Arial,sans-serif;font-weight:600;color:var(--slate);white-space:nowrap;position:absolute}
.brand-white{color:var(--white)}
.head{font-family:"Hind",Arial,sans-serif;font-weight:700;position:absolute;white-space:nowrap}
.tiny{position:absolute;font-size:6.4px;line-height:1.55;color:var(--text);text-align:justify}
.photo{position:absolute}
.pill{position:absolute;border-radius:10px;color:#fff;font-size:7px;text-align:center;font-family:"Open Sans",Arial,sans-serif}
.pagenum{position:absolute;right:12px;bottom:8px;width:16px;height:16px;border-radius:50%;color:#fff;font-size:6px;line-height:16px;text-align:center}
.dot{position:absolute;width:11px;height:11px;border-radius:50%;border:1px solid currentColor}
.rail{position:absolute;inset:0;background:linear-gradient(90deg,#8a929b,#c9cdd1)}
.field{position:absolute;left:118px;top:0;right:0;bottom:0;border-left:6px solid #fff;border-top:6px solid #fff;border-top-left-radius:90px;margin-top:-6px}
.card{position:absolute;left:44px;top:47px;width:162px;height:226px;border-radius:14px 14px 40px 14px;box-shadow:4px 6px 10px rgba(0,0,0,.3)}
.sec-label{position:absolute;right:28px;top:44px;font-size:7px;color:#fff}
.sec-title{position:absolute;right:28px;top:54px;font-family:"Hind",Arial,sans-serif;font-weight:700;font-size:31px;color:#fff;line-height:1}
.sec-rule{position:absolute;right:28px;top:92px;height:2px;background:#fff}
.sec-sub{position:absolute;right:28px;top:107px;font-size:8px;font-weight:700;color:#fff}
.sec-icon{position:absolute;top:48px}
.sec-foot{position:absolute;right:18px;bottom:20px;font-family:"Hind",Arial,sans-serif;font-weight:600;font-size:10px;color:#fff}
.band{position:absolute;left:0;top:0;width:498px;height:74px;border-bottom-right-radius:44px}
.body{position:absolute;left:0;top:52px;right:0;bottom:0;background:#fff;border-top-left-radius:44px}
.band-title{position:absolute;left:42px;top:12px;font-family:"Hind",Arial,sans-serif;font-weight:700;font-size:21px;color:#fff}
.corner-brand{position:absolute;right:10px;top:24px;font-family:"Hind",Arial,sans-serif;font-weight:600;font-size:8.5px;color:var(--slate)}
.subhead{position:absolute;font-size:7.5px;font-weight:600;color:#7a7f85;letter-spacing:.2px}
.caption{position:absolute;left:0;width:1200px;top:2818px;text-align:center;font-family:"Open Sans",Arial,sans-serif;font-size:17px;color:#444}
</style>
</head>
<body>

<section class="slide col-l r1">
  <div class="brand" style="left:0;width:568px;text-align:center;top:142px;font-size:32px">Terraquest NW</div>
</section>

<section class="slide col-r r1">
  <div class="photo" role="img" aria-label="Aerial photograph of an open-pit mine in grey rock" style="left:0;top:58px;width:568px;height:262px;background:linear-gradient(135deg,#69737d,#4d5761 55%,#5f6972);border-top-left-radius:60px"></div>
  <div style="position:absolute;right:0;top:0;width:90px;height:80px;background:#fff;border-bottom-left-radius:60px"></div>
  <div class="brand" style="left:0;width:568px;text-align:center;top:24px;font-size:15px">Terraquest NW</div>
  <div style="position:absolute;left:0;width:568px;top:94px;text-align:center;color:#fff;font-size:7.5px;letter-spacing:3px">www.terraquestnw.org</div>
  <div class="head" style="left:0;width:568px;text-align:center;top:110px;font-size:30px;color:#fff">Master Slide Presentation</div>
  <div style="position:absolute;left:0;width:568px;top:152px;text-align:center;color:#fff;font-size:7.5px;letter-spacing:3px">subtitle goes here</div>
  <div class="pill" style="left:224px;top:244px;width:118px;height:14px;line-height:14px;background:#fff;color:var(--slate);font-size:6.5px">PRESENTER NAME</div>
  <div style="position:absolute;left:0;width:568px;top:268px;text-align:center;color:#fff;font-size:7px;font-weight:700">2020</div>
  <div class="dot" style="left:263px;top:288px;color:#fff"></div>
  <div class="dot" style="left:279px;top:288px;color:#fff"></div>
  <div class="dot" style="left:295px;top:288px;color:#fff"></div>
</section>

<section class="slide col-l r2">
  <div class="photo" role="img" aria-label="Faded photograph of snowy mountain peaks" style="left:250px;top:0;right:0;bottom:0;background:linear-gradient(160deg,#f6f6f7 20%,#e9e3e2 70%,#f3f3f4)"></div>
  <div class="brand" style="left:30px;top:130px;font-size:27px">Terraquest NW</div>
  <div style="position:absolute;left:247px;top:22px;width:2px;height:274px;background:var(--slate)"></div>
  <div class="head" style="right:24px;top:26px;font-size:30px;color:var(--slate);text-align:right;line-height:1.25">Presentation<br>Title here</div>
  <div style="position:absolute;right:22px;top:106px;font-size:7px;letter-spacing:3px;font-weight:600;color:var(--orange)">SUBTITLE GOES <span style="color:var(--blue)">HERE</span></div>
  <div class="pill" style="left:432px;top:259px;width:118px;height:13px;line-height:13px;background:var(--orange);font-size:6.5px">PRESENTER NAME</div>
  <div class="dot" style="left:508px;top:287px;color:var(--blue)"></div>
  <div class="dot" style="left:522px;top:287px;color:var(--blue)"></div>
  <div class="dot" style="left:536px;top:287px;color:var(--blue)"></div>
</section>

<section class="slide col-r r2">
  <div class="rail"></div>
  <div class="field" style="background:linear-gradient(90deg,#e9782d,#d55f1c)"></div>
  <div class="card photo" role="img" aria-label="Aerial photograph of a grey quarry with conveyor" style="background:linear-gradient(150deg,#8d9499,#5b6166 60%,#777d81)"></div>
  <svg class="sec-icon" style="left:354px;top:46px" width="52" height="52" viewBox="0 0 52 52" fill="none" stroke="#fff" stroke-width="2.2" stroke-linecap="round"><path d="M6 20 Q24 2 46 10"/><path d="M26 8 L12 48"/><path d="M30 20 L46 46"/></svg>
  <div class="sec-label">Section 01</div>
  <div class="sec-title">Minerals</div>
  <div class="sec-rule" style="width:50px"></div>
  <div class="sec-foot">Terraquest NW</div>
</section>

<section class="slide col-l r3">
  <div class="rail"></div>
  <div class="field" style="background:linear-gradient(90deg,#27ad4f,#1c9f45)"></div>
  <div class="card photo" role="img" aria-label="Photograph of an oil pump jack at sunset" style="background:linear-gradient(180deg,#d7a24a,#a8692a 55%,#3d2a1a)"></div>
  <svg class="sec-icon" style="left:392px" width="44" height="54" viewBox="0 0 44 54" fill="none" stroke="#fff" stroke-width="2" stroke-linecap="round"><circle cx="22" cy="24" r="12"/><path d="M16 36h12M17 41h10M19 46h6"/><path d="M22 2v4M6 10l3 3M38 10l-3 3M2 24h4M42 24h-4"/></svg>
  <div class="sec-label">Section 02</div>
  <div class="sec-title">Energy</div>
  <div class="sec-rule" style="width:50px"></div>
  <div class="sec-sub">OIL &amp; GAS</div>
  <div class="sec-foot">Terraquest NW</div>
</section>

<section class="slide col-r r3">
  <div class="rail"></div>
  <div class="field" style="background:linear-gradient(90deg,#7cc242,#8ccb4f)"></div>
  <div class="card photo" role="img" aria-label="Photograph of a green seedling sprouting from soil" style="background:linear-gradient(180deg,#8fbf5a,#4e5a36 45%,#3b322b)"></div>
  <svg class="sec-icon" style="left:392px" width="44" height="54" viewBox="0 0 44 54" fill="none" stroke="#fff" stroke-width="2" stroke-linecap="round"><circle cx="22" cy="24" r="12"/><path d="M16 36h12M17 41h10M19 46h6"/><path d="M22 2v4M6 10l3 3M38 10l-3 3M2 24h4M42 24h-4"/></svg>
  <div class="sec-label">Section 03</div>
  <div class="sec-title">Energy</div>
  <div class="sec-rule" style="width:50px"></div>
  <div class="sec-sub">GEOTHERMAL</div>
  <div class="sec-foot">Terraquest NW</div>
</section>

<section class="slide col-l r4">
  <div class="rail"></div>
  <div class="field" style="background:linear-gradient(90deg,#29a7cd,#2aa2c6)"></div>
  <div class="card photo" role="img" aria-label="Photograph of a water droplet and ripples" style="background:linear-gradient(180deg,#dfe9f0,#7fa8c9 45%,#2f6ea8)"></div>
  <svg class="sec-icon" style="left:408px;top:44px" width="44" height="58" viewBox="0 0 44 58" fill="none" stroke="#fff" stroke-width="2.2"><path d="M22 4 C30 18 40 28 40 38 A18 18 0 0 1 4 38 C4 28 14 18 22 4Z"/><path d="M12 40 a10 10 0 0 0 8 9" stroke-linecap="round"/></svg>
  <div class="sec-label">Section 04</div>
  <div class="sec-title">Water</div>
  <div class="sec-rule" style="width:50px"></div>
  <div class="sec-foot">Terraquest NW</div>
</section>

<section class="slide col-r r4">
  <div class="photo" role="img" aria-label="Photograph of a helicopter landed on orange rocky terrain" style="inset:0;background:linear-gradient(120deg,#b8692d,#6d4a2e 40%,#3b4550 70%,#c07a3a)"></div>
  <div style="position:absolute;left:40px;top:78px;width:312px;height:200px;background:rgba(110,118,128,.88);border-top-left-radius:38px"></div>
  <div style="position:absolute;left:78px;top:47px;width:325px;height:207px;border:1.5px solid rgba(255,255,255,.85);border-radius:10px 10px 30px 10px"></div>
  <div class="brand brand-white" style="left:265px;top:107px;font-size:10px">Terraquest NW</div>
  <div class="head" style="left:94px;top:185px;font-size:28px;color:#fff">Section break</div>
  <div style="position:absolute;left:94px;top:226px;width:48px;height:2px;background:#fff"></div>
</section>

<section class="slide col-l r5">
  <div class="band" style="background:var(--orange-soft)"></div>
  <div class="body"></div>
  <div class="band-title">Add Your Title Here</div>
  <div class="corner-brand">Terraquest NW</div>
  <div class="pill" style="left:24px;top:68px;width:115px;height:12px;line-height:12px;background:var(--orange);font-size:6px">ADD YOUR SUBTITLE HERE</div>
  <p class="tiny" style="left:32px;top:82px;width:300px">Lorem ipsum dolor sit amet, consectetuer adipiscing elit, sed diam nonummy nibh euismod tincidunt ut laoreet dolore magna aliquam erat volutpat. Ut wisi enim ad minim veniam, quis nostrud exerci tation ullamcorper suscipit lobortis nisl ut aliquip ex ea commodo consequat. Duis autem vel eum iriure dolor in hendrerit in vulputate velit esse molestie consequat, vel illum dolore eu feugiat nulla facilisis at vero eros et accumsan et.</p>
  <div class="pill" style="left:24px;top:194px;width:115px;height:12px;line-height:12px;background:var(--slate);font-size:6px">ADD YOUR SUBTITLE HERE</div>
  <p class="tiny" style="left:32px;top:208px;width:300px">Lorem ipsum dolor sit amet, consectetuer adipiscing elit, sed diam nonummy nibh euismod tincidunt ut laoreet dolore magna aliquam erat volutpat. Ut wisi enim ad minim veniam, quis nostrud exerci tation ullamcorper suscipit lobortis nisl ut aliquip ex ea commodo consequat. Duis autem vel eum iriure dolor in hendrerit in vulputate velit esse molestie consequat, vel illum dolore eu feugiat nulla facilisis at vero eros et accumsan et.</p>
  <div style="position:absolute;left:345px;top:66px;width:2px;height:240px;background:var(--slate)"></div>
  <div class="photo" role="img" aria-label="Photograph of a brown and gold mineral specimen" style="left:368px;top:68px;width:136px;height:106px;border-radius:10px;background:linear-gradient(135deg,#8a5a2c,#c9954a 50%,#5a3a20);box-shadow:2px 4px 6px rgba(0,0,0,.25)"></div>
  <div class="photo" role="img" aria-label="Photograph of white quartz crystals" style="left:368px;top:189px;width:136px;height:108px;border-radius:10px;background:linear-gradient(135deg,#9a948a,#dcd8d0 50%,#6c6860);box-shadow:2px 4px 6px rgba(0,0,0,.25)"></div>
  <div class="pagenum" style="background:var(--orange)">9</div>
</section>

<section class="slide col-r r5">
  <div class="band" style="background:var(--green)"></div>
  <div class="body"></div>
  <div class="band-title">Add Your Title Here</div>
  <div class="corner-brand">Terraquest NW</div>
  <div class="photo" role="img" aria-label="Illustration of a magnifying glass with a lightbulb inside" style="left:14px;top:96px;width:214px;height:166px;border-radius:10px;background:linear-gradient(135deg,#eef1ee,#d9dedb 60%,#cfe6d5)"></div>
  <div style="position:absolute;left:264px;top:76px;width:2px;height:72px;background:var(--green)"></div>
  <div class="subhead" style="left:280px;top:82px;color:var(--green);font-size:6.5px">ADD YOUR SUBTITLE HERE</div>
  <p class="tiny" style="left:280px;top:91px;width:240px;text-align:left">Lorem ipsum dolor sit amet, consectetuer adipiscing elit, sed diam nonummy nibh euismod tincidunt ut laoreet dolore magna aliquam erat volutpat.</p>
  <div style="position:absolute;left:264px;top:154px;width:2px;height:72px;background:var(--lime)"></div>
  <div class="subhead" style="left:280px;top:160px;color:var(--lime);font-size:6.5px">ADD YOUR SUBTITLE HERE</div>
  <p class="tiny" style="left:280px;top:169px;width:240px;text-align:left">Lorem ipsum dolor sit amet, consectetuer adipiscing elit, sed diam nonummy nibh euismod tincidunt ut laoreet dolore magna aliquam erat volutpat.</p>
  <div style="position:absolute;left:264px;top:232px;width:2px;height:72px;background:var(--slate)"></div>
  <div class="subhead" style="left:280px;top:238px;font-size:6.5px">ADD YOUR SUBTITLE HERE</div>
  <p class="tiny" style="left:280px;top:247px;width:240px;text-align:left">Lorem ipsum dolor sit amet, consectetuer adipiscing elit, sed diam nonummy nibh euismod tincidunt ut laoreet dolore magna aliquam erat volutpat.</p>
  <div class="pagenum" style="background:var(--green)">10</div>
</section>

<section class="slide col-l r6">
  <div class="band" style="background:var(--lime)"></div>
  <div class="body"></div>
  <div class="band-title">Add Your Title Here</div>
  <div class="corner-brand">Terraquest NW</div>
  <div class="photo" role="img" aria-label="Photograph of a green seedling in dark soil" style="left:25px;top:76px;width:162px;height:226px;border-radius:14px 14px 40px 14px;background:linear-gradient(180deg,#93c266,#51613a 40%,#3c332c);box-shadow:3px 5px 8px rgba(0,0,0,.28)"></div>
  <div style="position:absolute;left:218px;top:76px;width:2px;height:226px;background:var(--lime)"></div>
  <div class="head" style="left:240px;top:90px;font-size:26px;color:#b7d13b">05.</div>
  <div class="pill" style="left:236px;top:130px;width:124px;height:15px;line-height:15px;border:1px solid #e4e4e4;color:#b7d13b;font-size:8px">Add your subtitle here</div>
  <p class="tiny" style="left:240px;top:154px;width:286px">Lorem ipsum dolor sit amet, consectetuer adipiscing elit, sed diam nonummy nibh euismod tincidunt ut laoreet dolore magna aliquam erat volutpat. Ut wisi enim ad minim veniam, quis nostrud exerci tation ullamcorper suscipit lobortis nisl ut aliquip ex ea commodo consequat. Duis autem vel eum iriure dolor in hendrerit in vulputate velit esse molestie consequat, vel illum dolore eu feugiat nulla facilisis at vero eros et accumsan et iusto odio dignissim qui blandit praesent luptatum zzril delenit augue duis dolore te feugait nulla facilisi.</p>
  <div class="pagenum" style="background:var(--lime)">11</div>
</section>

<section class="slide col-r r6">
  <div class="band" style="background:var(--blue)"></div>
  <div class="body"></div>
  <div class="band-title">Add Your Title Here</div>
  <div class="corner-brand">Terraquest NW</div>
  <div class="subhead" style="left:35px;top:102px">ADD YOUR SUBTITLE HERE</div>
  <p class="tiny" style="left:35px;top:114px;width:232px">Lorem ipsum dolor sit amet, consectetuer adipiscing elit, sed diam nonummy nibh euismod tincidunt ut laoreet dolore magna aliquam erat volutpat. Ut wisi enim ad minim veniam, quis nostrud exerci tation ullamcorper suscipit lobortis nisl ut aliquip ex ea commodo consequat. Duis autem vel eum iriure dolor in hendrerit in vulputate velit esse molestie consequat, vel illum dolore eu feugiat nulla facilisis at vero eros et accumsan et iusto odio dignissim qui blandit praesent luptatum zzril delenit augue duis dolore te feugait nulla facilisi.</p>
  <div class="pill" style="left:32px;top:280px;width:76px;height:13px;line-height:13px;border-radius:0;background:var(--blue);font-size:6.5px;letter-spacing:1.5px">LEARN MORE</div>
  <div class="subhead" style="left:295px;top:102px">ADD YOUR SUBTITLE HERE</div>
  <p class="tiny" style="left:295px;top:114px;width:232px">Lorem ipsum dolor sit amet, consectetuer adipiscing elit, sed diam nonummy nibh euismod tincidunt ut laoreet dolore magna aliquam erat volutpat. Ut wisi enim ad minim veniam, quis nostrud exerci tation ullamcorper suscipit lobortis nisl ut aliquip ex ea commodo consequat. Duis autem vel eum iriure dolor in hendrerit in vulputate velit esse molestie consequat, vel illum dolore eu feugiat nulla facilisis at vero eros et accumsan et iusto odio dignissim qui blandit praesent luptatum zzril delenit augue duis dolore te feugait nulla facilisi.</p>
  <div class="pill" style="left:292px;top:280px;width:76px;height:13px;line-height:13px;border-radius:0;background:var(--blue);font-size:6.5px;letter-spacing:1.5px">LEARN MORE</div>
  <div class="pagenum" style="background:var(--blue)">12</div>
</section>

<section class="slide col-l r7">
  <div style="position:absolute;left:0;top:0;width:34px;height:320px;background:linear-gradient(180deg,#e98a4c,#d55f1c);border-top-right-radius:34px"></div>
  <div class="head" style="left:8px;top:222px;transform:rotate(-90deg);transform-origin:0 0;font-size:19px;color:#fff">Map Option <span style="font-family:'Open Sans',Arial,sans-serif;font-weight:400;font-size:7px">With all 4 colors</span></div>
  <div style="position:absolute;left:48px;top:36px;width:444px;height:272px;border:1px solid #2b8fbf"></div>
  <div style="position:absolute;left:58px;top:42px;font-size:8px;color:var(--green)">This map not include, just an Ex.</div>
  <div class="photo" role="img" aria-label="Map of natural regions and national parks across the country" style="left:50px;top:56px;width:440px;height:250px;background:linear-gradient(135deg,#e8f3f8,#f5f0d8 40%,#eef4e0 70%,#dceef6)"></div>
  <div class="corner-brand" style="top:16px">Terraquest NW</div>
  <div style="position:absolute;left:489px;top:68px;width:50px;height:82px;background:var(--orange-soft)"></div>
  <div class="head" style="left:496px;top:74px;font-size:17px;font-weight:500;color:#fff;line-height:1">Map<br>&nbsp;&nbsp;01</div>
  <div style="position:absolute;left:528px;top:74px;width:2px;height:40px;background:#fff"></div>
  <p class="tiny" style="left:489px;top:156px;width:66px;text-align:left">Lorem ipsum dolor sit amet, consectetuer adipiscing elit, sed diam nonummy nibh euismod tincidunt ut laoreet dolore magna aliquam erat volutpat. Ut wisi enim ad minim veniam, quis nostrud exerci tation ullamcorper suscipit lobortis nisl ut aliquip ex ea commodo consequat.</p>
  <div class="pagenum" style="background:var(--orange)">13</div>
</section>

<section class="slide col-r r7">
  <div class="corner-brand" style="top:18px">Terraquest NW</div>
  <div class="head" style="left:37px;top:72px;font-size:21px;color:var(--orange)">Title Goes <span style="color:var(--blue)">Here</span></div>
  <div style="position:absolute;left:38px;top:102px;font-size:7.5px;letter-spacing:3px;font-weight:600;color:#777">SUBTITLE GOES HERE</div>
  <p class="tiny" style="left:38px;top:136px;width:194px">Lorem ipsum dolor sit amet, consectetuer adipiscing elit, sed diam nonummy nibh euismod tincidunt ut laoreet dolore magna aliquam erat volutpat. Ut wisi enim ad minim veniam, quis nostrud exerci tation ullamcorper suscipit lobortis nisl ut aliquip ex ea commodo consequat.</p>
  <div style="position:absolute;left:302px;top:22px;width:2px;height:246px;background:#8a9096"></div>
  <div style="position:absolute;left:284px;top:38px;width:38px;height:38px;border-radius:50%;background:var(--orange);border:4px solid #e6e6e6"></div>
  <div style="position:absolute;left:284px;top:98px;width:38px;height:38px;border-radius:50%;background:var(--green);border:4px solid #e6e6e6"></div>
  <div style="position:absolute;left:284px;top:158px;width:38px;height:38px;border-radius:50%;background:var(--lime);border:4px solid #e6e6e6"></div>
  <div style="position:absolute;left:284px;top:219px;width:38px;height:38px;border-radius:50%;background:var(--blue);border:4px solid #e6e6e6"></div>
  <svg style="position:absolute;left:284px;top:38px" width="38" height="230" viewBox="0 0 38 230" fill="none" stroke="#fff" stroke-width="1.6" stroke-linecap="round">
    <circle cx="19" cy="14" r="3"/><circle cx="13" cy="24" r="3"/><circle cx="25" cy="24" r="3"/>
    <circle cx="19" cy="79" r="6"/><path d="M19 69v3M19 86v3M9 79h3M26 79h3"/>
    <rect x="12" y="132" width="14" height="14" rx="3"/><path d="M16 139h6"/>
    <path d="M12 206l14-14M14 198a5 5 0 0 1 8-6M24 200a5 5 0 0 1-8 6"/>
  </svg>
  <p class="tiny" style="left:342px;top:48px;width:150px;text-align:left;font-size:7px">Lorem Ipsum is simply dummy text of the printing and typesetting industry</p>
  <p class="tiny" style="left:342px;top:108px;width:150px;text-align:left;font-size:7px">Lorem Ipsum is simply dummy text of the printing and typesetting industry</p>
  <p class="tiny" style="left:342px;top:168px;width:150px;text-align:left;font-size:7px">Lorem Ipsum is simply dummy text of the printing and typesetting industry</p>
  <p class="tiny" style="left:342px;top:229px;width:150px;text-align:left;font-size:7px">Lorem Ipsum is simply dummy text of the printing and typesetting industry</p>
  <div class="pagenum" style="background:var(--slate)">14</div>
</section>

<section class="slide col-l r8">
  <div style="position:absolute;left:-80px;top:-6px;width:330px;height:330px;border-radius:50%;background:#d3d6da"></div>
  <div class="photo" role="img" aria-label="Photograph of a hiker crouching on a mountain ridge" style="left:-80px;top:-12px;width:318px;height:340px;border-radius:0 50% 50% 0;background:linear-gradient(160deg,#6b7680,#47524a 50%,#7d7560)"></div>
  <div class="head" style="left:24px;top:88px;font-size:21px;color:#fff;line-height:1.25">Our<br>Process<br>Steps</div>
  <div class="corner-brand" style="top:20px">Terraquest NW</div>
  <div style="position:absolute;left:230px;top:10px;width:36px;height:36px;border-radius:50%;background:var(--slate);border:4px solid var(--orange);color:#fff;font-size:13px;font-weight:700;line-height:28px;text-align:center">01</div>
  <p class="tiny" style="left:283px;top:14px;width:190px;text-align:left;font-size:7px">Lorem Ipsum is simply dummy text of the printing and typesetting industry</p>
  <div style="position:absolute;left:270px;top:64px;width:36px;height:36px;border-radius:50%;background:var(--slate);border:4px solid var(--green);color:#fff;font-size:13px;font-weight:700;line-height:28px;text-align:center">02</div>
  <p class="tiny" style="left:326px;top:66px;width:190px;text-align:left;font-size:7px">Lorem Ipsum is simply dummy text of the printing and typesetting industry</p>
  <div style="position:absolute;left:293px;top:120px;width:36px;height:36px;border-radius:50%;background:var(--slate);border:4px solid var(--lime);color:#fff;font-size:13px;font-weight:700;line-height:28px;text-align:center">03</div>
  <p class="tiny" style="left:348px;top:122px;width:190px;text-align:left;font-size:7px">Lorem Ipsum is simply dummy text of the printing and typesetting industry</p>
  <div style="position:absolute;left:293px;top:176px;width:36px;height:36px;border-radius:50%;background:var(--slate);border:4px solid var(--blue);color:#fff;font-size:13px;font-weight:700;line-height:28px;text-align:center">04</div>
  <p class="tiny" style="left:348px;top:182px;width:190px;text-align:left;font-size:7px">Lorem Ipsum is simply dummy text of the printing and typesetting industry</p>
  <div style="position:absolute;left:270px;top:231px;width:36px;height:36px;border-radius:50%;background:var(--slate);border:4px solid var(--orange);color:#fff;font-size:13px;font-weight:700;line-height:28px;text-align:center">05</div>
  <p class="tiny" style="left:326px;top:235px;width:200px;text-align:left;font-size:7px">Lorem Ipsum is simply dummy text of the printing and typesetting industry</p>
  <div style="position:absolute;left:230px;top:276px;width:36px;height:36px;border-radius:50%;background:var(--slate);border:4px solid var(--green);color:#fff;font-size:13px;font-weight:700;line-height:28px;text-align:center">06</div>
  <p class="tiny" style="left:283px;top:282px;width:200px;text-align:left;font-size:7px">Lorem Ipsum is simply dummy text of the printing and typesetting industry</p>
  <div class="pagenum" style="background:#b9bec4">15</div>
</section>

<section class="slide col-r r8">
  <div class="head" style="left:55px;top:44px;font-size:24px;font-weight:600;color:var(--slate)">THANK YOU</div>
  <div style="position:absolute;left:58px;top:83px;font-size:8px;color:var(--orange)">Presenter <span style="color:var(--blue)">Name Here</span></div>
  <div class="brand" style="left:380px;top:50px;font-size:20px">Terraquest NW</div>
  <div class="photo" role="img" aria-label="Textured grey rock background" style="left:0;top:150px;width:568px;height:170px;background:linear-gradient(135deg,#626b75,#535c66 60%,#5d6670)"></div>
  <svg style="position:absolute;left:42px;top:200px" width="18" height="100" viewBox="0 0 18 100" fill="none" stroke="#fff" stroke-width="1.6" stroke-linecap="round" stroke-linejoin="round">
    <path d="M3 2l4 0 2 4-2 2a9 9 0 0 0 5 5l2-2 4 2v4a2 2 0 0 1-2 1A15 15 0 0 1 2 4a2 2 0 0 1 1-2z"/>
    <circle cx="9" cy="31" r="7"/><path d="M2 31h14M9 24c-3 4-3 10 0 14M9 24c3 4 3 10 0 14"/>
    <rect x="2" y="50" width="14" height="10" rx="1"/><path d="M2 51l7 5 7-5"/>
    <path d="M9 88s-6-6-6-10a6 6 0 0 1 12 0c0 4-6 10-6 10z"/><circle cx="9" cy="78" r="2"/>
  </svg>
  <div style="position:absolute;left:70px;top:203px;font-size:8px;color:#fff">(555) 014 2290</div>
  <div style="position:absolute;left:70px;top:227px;font-size:8px;color:#fff">www.terraquestnw.org</div>
  <div style="position:absolute;left:70px;top:251px;font-size:8px;color:#fff">info@terraquestnw.org</div>
  <div style="position:absolute;left:70px;top:274px;font-size:7.5px;color:#fff;white-space:nowrap">Terraquest NW, Suite 410 – 88 Harbourline Ave, Northport, British Columbia, V0X 1A0, Canada</div>
</section>

<div class="caption">both Letter-size and 16:9 include</div>

</body>
</html>
```